Stationary and Business Card for a Car leasing company
Brivo Motor Rentals LLC
Modern
Owen Ferrick
President
418 Halden Ridge Road
Pallisburg, NY 10847
oferrick@brivomotorrentals.com
Change the title of the "Cell Phone" to phone. There are two contact phone numbers.
** want a plain business card (generic) with no personal information - just business name, contact address and phone numbers

```html
<!DOCTYPE html>
<html lang="en">
<head>
<meta charset="utf-8">
<title>Brivo Motor Rentals LLC — Business Card</title>
<link rel="stylesheet" href="https://fonts.googleapis.com/css2?family=Montserrat:wght@400;600;800&display=swap">
<style>
  :root {
    --bg: #e4e5e7;
    --blue: #1d2fb8;
    --blue-deep: #121f8c;
    --blue-light: #3a55e0;
    --white: #ffffff;
    --navy: #0e1652;
    --ink: #3a3d4a;
    --muted: #6c6f7c;
  }
  * { margin: 0; padding: 0; box-sizing: border-box; }
  html, body { width: 1200px; height: 987px; overflow: hidden; }
  body {
    background: var(--bg);
    font-family: "Montserrat", sans-serif;
    position: relative;
  }
  .card {
    position: absolute;
    width: 620px;
    height: 354px;
    border-radius: 22px;
    overflow: hidden;
    box-shadow: 0 14px 30px rgba(0,0,0,0.18);
  }
  .card-front {
    left: 170px;
    top: 110px;
    background: linear-gradient(135deg, var(--blue-light), var(--blue) 55%, var(--blue-deep));
  }
  .skyline-area {
    position: absolute;
    left: 0;
    bottom: 0;
    width: 320px;
    height: 290px;
    background: linear-gradient(180deg, #e6e9f8, #ffffff);
  }
  .front-name {
    position: absolute;
    right: 36px;
    bottom: 34px;
    width: 240px;
    text-align: right;
    font-weight: 800;
    font-size: 26px;
    line-height: 1.15;
    color: var(--white);
    letter-spacing: 0.3px;
  }
  .card-back {
    left: 410px;
    top: 520px;
    background: var(--white);
  }
  .card-back svg.waves {
    position: absolute;
    inset: 0;
  }
  .brand {
    position: absolute;
    left: 34px;
    top: 40px;
    width: 230px;
    font-weight: 800;
    font-size: 26px;
    line-height: 1.1;
    color: var(--navy);
  }
  .person {
    position: absolute;
    left: 34px;
    top: 200px;
  }
  .person-name {
    font-weight: 600;
    font-size: 14px;
    color: var(--ink);
  }
  .person-title {
    font-weight: 400;
    font-size: 11px;
    color: var(--muted);
    margin-top: 2px;
  }
  .contacts {
    position: absolute;
    left: 330px;
    top: 178px;
    list-style: none;
  }
  .contacts li {
    display: flex;
    align-items: center;
    gap: 7px;
    font-size: 10px;
    color: var(--ink);
    line-height: 17px;
    white-space: nowrap;
  }
  .contacts .indent { padding-left: 19px; }
  .icon {
    width: 12px;
    height: 12px;
    flex: none;
  }
</style>
</head>
<body>

  <section class="card card-front" aria-label="Business card front">
    <div class="skyline-area" role="img" aria-label="White city skyline silhouette"></div>
    <div class="front-name">Brivo Motor Rentals LLC</div>
  </section>

  <section class="card card-back" aria-label="Business card back">
    <svg class="waves" width="620" height="354" viewBox="0 0 620 354" aria-hidden="true">
      <defs>
        <linearGradient id="waveBlue" x1="0" y1="0" x2="1" y2="1">
          <stop offset="0" stop-color="#3a55e0"/>
          <stop offset="1" stop-color="#121f8c"/>
        </linearGradient>
      </defs>
      <path d="M250 0 H620 V200 C520 150 420 60 250 0 Z" fill="url(#waveBlue)"/>
      <path d="M230 0 C400 50 510 150 620 215 V200 C520 150 420 60 250 0 Z" fill="#9aa6ee"/>
      <path d="M0 354 V336 C180 340 420 330 620 290 V354 Z" fill="url(#waveBlue)"/>
    </svg>

    <div class="brand">Brivo Motor Rentals LLC</div>

    <div class="person">
      <div class="person-name">Owen Ferrick</div>
      <div class="person-title">President</div>
    </div>

    <ul class="contacts">
      <li>
        <svg class="icon" viewBox="0 0 12 12" aria-hidden="true"><circle cx="6" cy="6" r="6" fill="var(--blue)"/><path d="M6 2.6a2.2 2.2 0 0 0-2.2 2.2C3.8 6.6 6 9.4 6 9.4s2.2-2.8 2.2-4.6A2.2 2.2 0 0 0 6 2.6z" fill="#fff"/></svg>
        418 Halden Ridge Road
      </li>
      <li class="indent">Pallisburg, NY 10847</li>
      <li>
        <svg class="icon" viewBox="0 0 12 12" aria-hidden="true"><circle cx="6" cy="6" r="6" fill="var(--blue)"/><path d="M4 3l1.2 1.6-.6.8c.4.9 1 1.5 1.9 1.9l.8-.6L9 8l-.6 1C6 9 3 6 3 3.6z" fill="#fff"/></svg>
        Phone: (845) 555-0142
      </li>
      <li>
        <svg class="icon" viewBox="0 0 12 12" aria-hidden="true"><circle cx="6" cy="6" r="6" fill="var(--blue)"/><path d="M4 3l1.2 1.6-.6.8c.4.9 1 1.5 1.9 1.9l.8-.6L9 8l-.6 1C6 9 3 6 3 3.6z" fill="#fff"/></svg>
        Phone: (845) 555-0178
      </li>
      <li>
        <svg class="icon" viewBox="0 0 12 12" aria-hidden="true"><circle cx="6" cy="6" r="6" fill="var(--blue)"/><rect x="3" y="4" width="6" height="4.2" fill="#fff"/><path d="M3 4l3 2.3L9 4" stroke="var(--blue)" stroke-width="0.7" fill="none"/></svg>
        oferrick@brivomotorrentals.com
      </li>
      <li>
        <svg class="icon" viewBox="0 0 12 12" aria-hidden="true"><circle cx="6" cy="6" r="6" fill="var(--blue)"/><circle cx="6" cy="6" r="3" stroke="#fff" stroke-width="0.8" fill="none"/><path d="M3 6h6M6 3v6" stroke="#fff" stroke-width="0.7"/></svg>
        www.brivomotorrentals.com
      </li>
    </ul>
  </section>

</body>
</html>
```